Business cards & Stationary design

We are a mortgage advisors and want our business cards to reflect our professional nature.
Our logo will be remaining the same and we want this to feature on the business cards.
We require both a back and front design.

On the back the following text needs to appear in VERY small print.

"Brackley Private Finance trading as The Harbourside Mortgage & Loan Company which is authorised and regulated by the Monetary Practices Board.

Brackley Private Finance Limited. Registered in England and Wales No: 04192***. Registered Office *************** (address will be disclosed when awarded)"

On the front, we want the logo and fields for employee name, job title and contact details

EG)

Peter Dawlish
Mortgage Broker
07921 308114
PeterDawlish@[url removed, login to view]

We are open to various designs however they MUST look professional and meet all the above requirements. We have attached photos of our website and a file for our logo.

Thanks.

```html
<!DOCTYPE html>
<html lang="en">
<head>
<meta charset="utf-8">
<title>The Harbourside Mortgage &amp; Loan Company – Business Cards</title>
<link href="https://fonts.googleapis.com/css2?family=Lato:wght@400;700&display=swap" rel="stylesheet">
<style>
  :root {
    --backdrop: #2b2b2d;
    --card-black: #050506;
    --card-navy: #13161e;
    --gold: #f2a81d;
    --rule-grey: #7b7b7d;
    --name-box: #5d5d5f;
    --white: #ffffff;
    --text-light: #e9e9ec;
    --fine-print: #9a9a9e;
  }
  * { box-sizing: border-box; margin: 0; padding: 0; }
  html, body { width: 1200px; height: 900px; overflow: hidden; }
  body {
    background: var(--backdrop);
    font-family: "Lato", Arial, sans-serif;
    position: relative;
  }
  .card {
    position: absolute;
    left: 285px;
    width: 630px;
    height: 360px;
    border-radius: 18px;
    overflow: hidden;
  }

  /* Logo side */
  .card--logo { top: 60px; background: var(--card-black); }
  .stripe-pair { position: absolute; left: 0; right: 0; }
  .stripe-pair--top { top: 72px; }
  .stripe-pair--bottom { top: 268px; }
  .stripe-gold { height: 6px; background: var(--gold); }
  .stripe-grey { height: 4px; margin-top: 6px; background: var(--rule-grey); }
  .company-name {
    position: absolute;
    top: 124px;
    left: 0; right: 0;
    text-align: center;
    font-family: "Lato", Arial, sans-serif;
    font-weight: 700;
    color: var(--gold);
    font-size: 28px;
    line-height: 1.2;
    letter-spacing: 1px;
    text-transform: uppercase;
  }
  .regulatory-note {
    position: absolute;
    left: 40px; right: 40px;
    bottom: 16px;
    font-size: 7.5px;
    line-height: 1.45;
    color: var(--fine-print);
    text-align: center;
  }
  .regulatory-note p + p { margin-top: 3px; }

  /* Contact side */
  .card--contact { top: 480px; background: var(--card-navy); }
  .city-photo {
    position: absolute;
    top: 0; left: 0; right: 0;
    height: 212px;
    background:
      radial-gradient(ellipse 120px 60px at 70% 60%, rgba(226,150,60,0.55), transparent 70%),
      radial-gradient(ellipse 140px 50px at 25% 80%, rgba(70,90,200,0.5), transparent 70%),
      radial-gradient(ellipse 90px 50px at 48% 55%, rgba(200,120,60,0.4), transparent 70%),
      linear-gradient(180deg, #1d1f2c 0%, #2a2633 45%, #3b2f2a 70%, #1a1d2a 100%);
  }
  .divider-line {
    position: absolute;
    top: 212px; left: 0; right: 0;
    height: 5px;
    background: var(--white);
  }
  .name-box {
    position: absolute;
    top: 232px;
    right: 30px;
    width: 175px;
    height: 60px;
    background: var(--name-box);
    color: var(--gold);
    text-align: center;
    padding-top: 11px;
  }
  .name-box .person-name { font-size: 17px; font-weight: 700; line-height: 1.1; }
  .name-box .job-title { font-size: 13px; font-weight: 700; margin-top: 3px; }
  .contact-list {
    position: absolute;
    top: 240px;
    left: 36px;
    list-style: none;
  }
  .contact-list li {
    display: flex;
    align-items: center;
    gap: 14px;
    color: var(--text-light);
    font-size: 15px;
    height: 33px;
  }
  .contact-list svg { width: 14px; height: 14px; fill: var(--text-light); flex: none; }
</style>
</head>
<body>

  <section class="card card--logo" aria-label="Business card, logo side">
    <div class="stripe-pair stripe-pair--top"><div class="stripe-gold"></div><div class="stripe-grey"></div></div>
    <div class="company-name">The Harbourside<br>Mortgage &amp; Loan<br>Company</div>
    <div class="stripe-pair stripe-pair--bottom"><div class="stripe-gold"></div><div class="stripe-grey"></div></div>
    <div class="regulatory-note">
      <p>Brackley Private Finance trading as The Harbourside Mortgage &amp; Loan Company which is authorised and regulated by the Monetary Practices Board.</p>
      <p>Brackley Private Finance Limited. Registered in England and Wales No: 04192***. Registered Office ***************</p>
    </div>
  </section>

  <section class="card card--contact" aria-label="Business card, contact side">
    <div class="city-photo" role="img" aria-label="Night-time photograph of a city riverside bridge with lights reflected in the water"></div>
    <div class="divider-line"></div>
    <div class="name-box">
      <div class="person-name">Peter Dawlish</div>
      <div class="job-title">Mortgage Broker</div>
    </div>
    <ul class="contact-list">
      <li>
        <svg viewBox="0 0 24 24" aria-hidden="true"><path d="M6.6 10.8a15.1 15.1 0 0 0 6.6 6.6l2.2-2.2c.3-.3.7-.4 1-.2 1.1.4 2.3.6 3.6.6.6 0 1 .4 1 1V20c0 .6-.4 1-1 1C10.6 21 3 13.4 3 4c0-.6.4-1 1-1h3.5c.6 0 1 .4 1 1 0 1.3.2 2.5.6 3.6.1.3 0 .7-.2 1z"/></svg>
        <span>07921 308114</span>
      </li>
      <li>
        <svg viewBox="0 0 24 24" aria-hidden="true"><path d="M2 5h20v14H2z M3.5 6.5 12 13l8.5-6.5" fill="none" stroke="#e9e9ec" stroke-width="2"/></svg>
        <span>PeterDawlish@HarbourBroker.net</span>
      </li>
      <li>
        <svg viewBox="0 0 24 24" aria-hidden="true"><circle cx="12" cy="12" r="9" fill="none" stroke="#e9e9ec" stroke-width="2"/><path d="M3 12h18M12 3c3 3 3 15 0 18M12 3c-3 3-3 15 0 18" fill="none" stroke="#e9e9ec" stroke-width="1.6"/></svg>
        <span>www.PeterDawlish.com</span>
      </li>
    </ul>
  </section>

</body>
</html>
```